Website design for Kelvora Quad

Full Website Content Draft for: 'Kelvora Quad - A Financial Freedom Movement'

Header / Navigation
Logo (top left)
Navigation Links: Home | Our Story | Current State | Future State | How You Can Help | The Movement | Get Involved
CTA Button: Join the Movement
Homepage (Hero Section)

Headline:
Empowering Students. Transforming Futures.
Sub-Headline:
Financial literacy isn’t optional anymore — it’s essential.
Body (short):
Every year, millions of college students step into adulthood without the skills to manage money wisely. It’s time to change that.
Call-to-Action Button:
[Join the Movement]
Visual Suggestion:
Full-width image/video of diverse students on campus — upbeat, collaborative, inspiring.
Our Story

Section Header: Our Story
Body Copy:
For too long, financial literacy has been the missing piece of higher education. While students prepare academically for their futures, many graduate with financial stress, poor money habits, and debt that follows them for decades.
We believe knowledge is power — and financial literacy is freedom. With decades of combined experience in banking, leadership, and higher education, our team has seen the struggles firsthand. That’s why we’re committed to starting a movement that ensures every student leaves college not only with a degree, but with financial confidence.
The Current State

Section Header: The Current State
Infographic Copy / Stats:
70% of college students report finances as their #1 source of stress.*
43% of students don’t know their credit score.**
Student loan debt has surpassed $1.7 trillion.***
Subtext:
This is today’s reality. Students deserve better.
Footnotes (to place at bottom of page):
* Continental Scholar Wellness Society, Nationwide Pupil Vitality Survey, Spring 2022 Report.
** DORLANX & PMQ Pension Solutions, Coin Sense in the Dorms Study (2019).
*** Central Lending Board of Tamsworth, Consumer Credit Data (2024).
Visual Suggestion:
Infographic row with 3 icons (stress, credit, debt) and corresponding stats.
The Future State (Vision)

Section Header: The Future State (Vision)
Body Copy:
Imagine a campus where students graduate with more than a degree — they graduate with financial confidence.
They know how to budget, save, manage credit, and plan for their futures. They are free from fear, better equipped for life after graduation, and ready to thrive personally and professionally.
This is the future we are building together.
Visual Suggestion:
Smiling students celebrating graduation, overlay text “Confidence. Knowledge. Freedom.”
How You Can Help

Section Header: How You Can Help
Copy with Columns:
Universities
Partner with us to bring scalable, student-centered financial education to your campus.
Banks & Financial Institutions
Join us in shaping the next generation of financially confident customers while strengthening community impact.
Students & Parents
Be part of a movement that makes the college experience stronger, not harder.
Call-to-Action Button:
[Contact Us to Partner]
Visual Suggestion:
Three-column layout with icons (graduation cap for Universities, bank building for Banks, heart/people for Students & Parents).
The Movement

Section Header: The Movement
Body Copy:
This isn’t about one campus — it’s about a shift. A national movement to change the financial future for an entire generation. Together, we can rewrite the story.
We believe when students understand money, they reduce stress, gain freedom, and unlock their potential. That’s why this is more than a program — it’s a movement.
Visual Suggestion:
Map of the U.S. with “movement dots” spreading out, or collage of diverse students with bold words: Financial Literacy. Confidence. Future.
Get Involved (Contact Section)

Section Header: Get Involved
Body Copy:
Are you a university leader, bank executive, student, or parent who wants to be part of this movement? Let’s talk.
Contact Form Fields:
Name
Email
Role (University Faculty/Staff, Bank Partner, Student, Parent, Other)
Message
CTA Button: [Submit Interest]
Footer

Copy:
Join us in building the future of financial literacy.
Links: Privacy | Contact | Social Media (WorkLoop, Pixmora, etc.)
for my new Web Design Project will be added soon.

Target Market(s)

Partners: University Faculty and Bank Executives

Industry/Entity Type

Finance and Education

Coding

Coded - Design and coding required

Number of Pages Required

4 page

Font styles to use
Sans Serif

Colors

Designer to choose colors to be used in the design.

Requirements
Nice to have
• See description for details - This is a website to create a "movement" to help college and university students increase their financial literacy and reduce financial stress,

```html
<!DOCTYPE html>
<html lang="en">
<head>
<meta charset="UTF-8">
<title>Kelvora Quad — A Financial Freedom Movement</title>
<link href="https://fonts.googleapis.com/css2?family=Montserrat:wght@400;500;600;700;800&display=swap" rel="stylesheet">
<style>
:root{
  --blue:#1a73d1;
  --blue-dark:#0d5fb8;
  --navy:#0a2c8c;
  --royal:#0d47c9;
  --ink:#1d1d1f;
  --text:#3a3a3a;
  --muted:#5d5d5d;
  --white:#ffffff;
  --line:#e3e6ea;
  --black:#0b0b0b;
}
*{box-sizing:border-box;margin:0;padding:0}
html,body{width:1200px;height:4396px;overflow:hidden}
body{font-family:'Montserrat',sans-serif;color:var(--ink);background:var(--white);position:relative}
section,header,footer{position:absolute;left:0;width:1200px}
.btn{display:inline-flex;align-items:center;justify-content:center;border-radius:26px;background:var(--blue);color:var(--white);font-size:15px;font-weight:500;text-decoration:none}
.btn-outline{background:transparent;border:1.5px solid var(--white)}
.photo{position:absolute;border-radius:12px;overflow:hidden}
.photo-caption{position:absolute;left:0;right:0;bottom:30px;text-align:center;color:var(--white);font-weight:600;font-size:20px}
h2{font-size:38px;font-weight:700;color:var(--ink)}
h2 .accent{color:var(--blue)}

/* header */
.site-header{top:0;height:82px;border-bottom:1px solid var(--line);display:flex;align-items:center;padding:0 60px}
.brand{font-size:26px;font-weight:800;color:var(--blue);display:flex;align-items:center;gap:8px}
.brand-square{width:14px;height:14px;background:var(--blue)}
.nav{display:flex;gap:40px;margin-left:46px;font-size:15px;color:var(--text)}
.nav .active{color:var(--blue);font-weight:600}
.nav .more::after{content:" ⌄"}
.site-header .btn{margin-left:auto;width:228px;height:48px}

/* hero */
.hero{top:82px;height:582px}
.hero-tag{position:absolute;left:113px;top:92px;font-size:17px;font-weight:500}
.hero h1{position:absolute;left:113px;top:130px;width:480px;font-size:41px;line-height:50px;font-weight:700}
.hero h1 .accent{color:var(--blue)}
.hero p{position:absolute;left:113px;top:296px;width:470px;font-size:17px;line-height:29px;color:var(--text)}
.hero .btn{position:absolute;left:113px;top:413px;width:228px;height:48px}
.hero .photo{left:614px;top:114px;width:512px;height:374px;background:linear-gradient(135deg,#2b4a3c,#6c8a80 45%,#b75b3a 70%,#1f2a30)}

/* story */
.story{top:664px;height:404px;background:linear-gradient(135deg,var(--blue) 0%,#1e78d6 60%,#2a83dd 100%);color:var(--white);text-align:center;border-bottom:3px solid var(--black)}
.story h2{color:var(--white);margin-top:72px;font-size:36px}
.story p{width:900px;margin:22px auto 0;font-size:16px;line-height:27px}
.story p+p{margin-top:16px}

/* current state */
.current{top:1068px;height:560px;text-align:center}
.current h2{margin-top:98px}
.current .sub{margin-top:10px;font-size:17px;color:var(--text)}
.stat{position:absolute;top:229px;width:251px;height:248px;border-radius:12px;border:1px solid var(--line);box-shadow:0 4px 10px rgba(0,0,0,.12);background:var(--white);padding:26px 24px}
.stat .icon{width:76px;height:76px;border-radius:50%;background:var(--blue);margin:0 auto;display:flex;align-items:center;justify-content:center}
.stat .num{font-size:30px;font-weight:700;margin-top:16px}
.stat .cap{font-size:13.5px;line-height:21px;color:var(--text);margin-top:10px}
.stat.featured{background:var(--blue);color:var(--white);border:none}
.stat.featured .icon{background:var(--white)}
.stat.featured .cap{color:var(--white)}

/* future */
.future{top:1628px;height:505px}
.future .photo{left:96px;top:52px;width:469px;height:344px;background:linear-gradient(160deg,#8aa07a,#3a3a3a 45%,#121212)}
.future .text{position:absolute;left:599px;top:28px;width:490px}
.future p{font-size:16px;line-height:27px;color:var(--text);margin-top:14px}
.future h2{margin-bottom:10px}
.future .btn{margin-top:28px;width:242px;height:50px}

/* help */
.help{top:2133px;height:632px;background:linear-gradient(120deg,var(--navy) 0%,var(--royal) 55%,#1b63df 100%);text-align:center;border-bottom:3px solid var(--black)}
.help h2{color:var(--white);margin-top:78px;font-size:36px}
.help-card{position:absolute;top:190px;width:250px;height:246px;background:var(--white);border-radius:10px;padding:26px 26px}
.help-card .icon{width:76px;height:76px;border-radius:50%;background:var(--blue);margin:0 auto;display:flex;align-items:center;justify-content:center}
.help-card h3{font-size:19px;font-weight:600;margin-top:18px;line-height:26px}
.help-card p{font-size:13.5px;line-height:21px;color:var(--muted);margin-top:14px}
.help .btn{position:absolute;left:481px;top:487px;width:232px;height:48px}

/* movement */
.movement{top:2765px;height:560px}
.movement .text{position:absolute;left:113px;top:130px;width:460px}
.movement p{font-size:16px;line-height:27px;color:var(--text);margin-top:22px}
.movement .btn{margin-top:30px;width:218px;height:50px}
.movement .photo{left:616px;top:147px;width:473px;height:343px;background:linear-gradient(150deg,#c9d3dc,#7e8fa0 40%,#34495e 80%)}

/* contact */
.contact{top:3325px;height:560px}
.form-panel{position:absolute;left:113px;top:37px;width:631px;height:455px;border-radius:12px;background:linear-gradient(160deg,var(--blue),var(--blue-dark));padding:58px 36px}
.field{background:var(--white);border-radius:5px;height:48px;font-size:14px;color:var(--text);padding:14px 18px}
.row{display:flex;gap:26px}
.row .field{flex:1}
.field.select{margin-top:24px;display:flex;justify-content:space-between}
.field.area{margin-top:24px;height:110px}
.form-panel .btn{position:absolute;left:220px;top:360px;width:190px;height:48px}
.contact .text{position:absolute;left:782px;top:160px;width:290px}
.contact p{font-size:16px;line-height:27px;color:var(--text);margin-top:14px}
.contact .btn{margin-top:20px;width:156px;height:50px}

/* footer */
.site-footer{top:3885px;height:511px;color:var(--white)}
.footer-bg{position:absolute;inset:0}
.footer-brand{position:absolute;left:113px;top:150px;font-size:40px;font-weight:700;line-height:46px}
.footer-brand span{display:block;font-size:27px;padding-left:54px}
.footer-tag{position:absolute;left:113px;top:270px;font-size:15.5px;line-height:22px}
.fcol{position:absolute;top:162px}
.fcol h4{font-size:18px;font-weight:600;margin-bottom:26px}
.fcol a{display:block;color:var(--white);text-decoration:none;font-size:15px;margin-bottom:22px}
.socials{display:flex;gap:12px;margin-top:6px}
.socials span{display:flex;align-items:center;gap:5px;font-size:11px}
.socials i{width:12px;height:12px;border-radius:50%;background:var(--white);display:block}
.badge{position:absolute;background:var(--white);border-radius:6px}
.copyright{position:absolute;left:0;bottom:0;width:1200px;height:52px;background:var(--black);display:flex;align-items:center;justify-content:center;font-size:13px}
</style>
</head>
<body>

<header class="site-header">
  <div class="brand"><span class="brand-square"></span>Kelvora</div>
  <nav class="nav">
    <span class="active">Home</span><span>Our Story</span><span>Current State</span><span>Future State</span><span>How You Can Help</span><span class="more">More</span>
  </nav>
  <a class="btn" href="#">Join the Movement</a>
</header>

<section class="hero">
  <div class="hero-tag">Empowering Students. Transforming Futures.</div>
  <h1><span class="accent">Financial literacy</span> isn’t optional anymore — it’s essential.</h1>
  <p>Every year, millions of college students step into adulthood without the skills to manage money wisely. It’s time to change that.</p>
  <a class="btn" href="#">Join the Movement</a>
  <div class="photo" role="img" aria-label="Photo of diverse college students working together around a laptop on campus"></div>
</section>

<section class="story">
  <h2>Our Story</h2>
  <p>For too long, financial literacy has been the missing piece of higher education. While students prepare academically for their futures, many graduate with financial stress, poor money habits, and debt that follows them for decades.</p>
  <p>We believe knowledge is power — and financial literacy is freedom. With decades of combined experience in banking, leadership, and higher education, our team has seen the struggles firsthand. That’s why we’re committed to starting a movement that ensures every student leaves college not only with a degree, but with financial confidence.</p>
</section>

<section class="current">
  <h2><span class="accent">The</span> Current State</h2>
  <div class="sub">This is today’s reality. Students deserve better.</div>
  <div class="stat featured" style="left:160px">
    <div class="icon"><svg width="40" height="40" viewBox="0 0 40 40"><circle cx="20" cy="12" r="6" fill="#1a73d1"/><path d="M9 34 L13 20 H27 L31 34 Z" fill="#1a73d1"/><path d="M8 8 L13 14 M32 8 L27 14" stroke="#1a73d1" stroke-width="2.5"/></svg></div>
    <div class="num">70%</div>
    <div class="cap">of college students report finances as their #1 source of stress.</div>
  </div>
  <div class="stat" style="left:473px">
    <div class="icon"><svg width="40" height="40" viewBox="0 0 40 40"><rect x="5" y="11" width="26" height="18" rx="3" fill="#fff"/><rect x="5" y="15" width="26" height="4" fill="#1a73d1"/><circle cx="30" cy="26" r="7" fill="#fff" stroke="#1a73d1" stroke-width="2"/><path d="M27 26 l2 2 l4-4" stroke="#1a73d1" stroke-width="2" fill="none"/></svg></div>
    <div class="num">43%</div>
    <div class="cap">of students don’t know their credit score.</div>
  </div>
  <div class="stat" style="left:783px">
    <div class="icon"><svg width="40" height="40" viewBox="0 0 40 40"><path d="M14 8 h12 l-3 6 c7 4 10 10 10 15 c0 5-4 7-13 7 s-13-2-13-7 c0-5 3-11 10-15 Z" fill="#fff"/><text x="20" y="30" text-anchor="middle" font-family="Montserrat,sans-serif" font-size="11" font-weight="700" fill="#1a73d1">$</text></svg></div>
    <div class="num">$1.7</div>
    <div class="cap">Student loan debt has surpassed $1.7 trillion.</div>
  </div>
</section>

<section class="future">
  <div class="photo" role="img" aria-label="Photo of smiling graduates in caps and gowns celebrating"><div class="photo-caption">Confidence. Knowledge. Freedom.</div></div>
  <div class="text">
    <h2><span class="accent">The</span> Future State</h2>
    <p>Imagine a campus where students graduate with more than a degree — they graduate with financial confidence.</p>
    <p>They know how to budget, save, manage credit, and plan for their futures. They are free from fear, better equipped for life after graduation, and ready to thrive personally and professionally.</p>
    <p>This is the future we are building together.</p>
    <a class="btn" href="#">Be Part of This Future</a>
  </div>
</section>

<section class="help">
  <h2>How You Can Help</h2>
  <div class="help-card" style="left:169px">
    <div class="icon"><svg width="40" height="40" viewBox="0 0 40 40"><path d="M20 8 L36 16 L20 24 L4 16 Z" fill="#fff"/><path d="M11 20 v8 c0 3 18 3 18 0 v-8 l-9 5 Z" fill="#fff"/></svg></div>
    <h3>Universities</h3>
    <p>Partner with us to bring scalable, student-centered financial education to your</p>
  </div>
  <div class="help-card" style="left:473px">
    <div class="icon"><svg width="40" height="40" viewBox="0 0 40 40"><path d="M20 6 L34 13 H6 Z" fill="#fff"/><rect x="9" y="16" width="4" height="13" fill="#fff"/><rect x="18" y="16" width="4" height="13" fill="#fff"/><rect x="27" y="16" width="4" height="13" fill="#fff"/><rect x="6" y="31" width="28" height="3" fill="#fff"/></svg></div>
    <h3>Banks &amp; Financial Institutions</h3>
    <p>Join us in shaping the next generation of financially</p>
  </div>
  <div class="help-card" style="left:777px">
    <div class="icon"><svg width="40" height="40" viewBox="0 0 40 40"><circle cx="20" cy="13" r="5" fill="#fff"/><circle cx="9" cy="16" r="3.5" fill="#fff"/><circle cx="31" cy="16" r="3.5" fill="#fff"/><path d="M12 32 c0-8 16-8 16 0 Z M3 30 c0-6 10-6 10 0 Z M27 30 c0-6 10-6 10 0 Z" fill="#fff"/></svg></div>
    <h3>Students &amp; Parents</h3>
    <p>Be part of a movement that makes the college experience stronger, not</p>
  </div>
  <a class="btn btn-outline" href="#">Contact Us to Partner</a>
</section>

<section class="movement">
  <div class="text">
    <h2><span class="accent">The</span> Movement</h2>
    <p>This isn’t about one campus — it’s about a shift. A national movement to change the financial future for an entire generation. Together, we can rewrite the story.</p>
    <p>We believe when students understand money, they reduce stress, gain freedom, and unlock their potential. That’s why this is more than a program — it’s a movement.</p>
    <a class="btn" href="#">Join the Movement</a>
  </div>
  <div class="photo" role="img" aria-label="Photo of four diverse smiling students outdoors"><div class="photo-caption">Financial Literacy. Confidence. Future.</div></div>
</section>

<section class="contact">
  <div class="form-panel">
    <div class="row"><div class="field">Name</div><div class="field">Email</div></div>
    <div class="field select"><span>Role</span><span>⌄</span></div>
    <div class="field area">Message</div>
    <a class="btn btn-outline" href="#">Submit Interest</a>
  </div>
  <div class="text">
    <h2><span class="accent">Get</span> Involved</h2>
    <p>Are you a university leader, bank executive, student, or parent who wants to be part of this movement? Let’s talk.</p>
    <a class="btn" href="#">Contact Us</a>
  </div>
</section>

<footer class="site-footer">
  <svg class="footer-bg" width="1200" height="511" viewBox="0 0 1200 511" preserveAspectRatio="none">
    <path d="M0 43 L710 77 L1200 0 V511 H0 Z" fill="#1a73d1"/>
    <path d="M0 40 L710 75 L1200 -3" stroke="#0b0b0b" stroke-width="3" fill="none"/>
  </svg>
  <div class="footer-brand">Kelvora<span>Quad</span></div>
  <div class="footer-tag">Join us in building the<br>future of financial literacy</div>
  <div class="fcol" style="left:423px">
    <h4>QUICK LINKS</h4>
    <a href="#">HOME</a><a href="#">FUTURE STATE</a><a href="#">HOW YOU CAN HELP</a><a href="#">THE MOVEMENT</a><a href="#">GET INVOLVED</a>
  </div>
  <div class="fcol" style="left:667px">
    <h4>LEGAL</h4>
    <a href="#">PRIVACY POLICY</a><a href="#">CONTACT</a>
    <div class="socials"><span><i></i>Pixmora</span><span><i></i>Friendlane</span><span><i></i>WorkLoop</span></div>
  </div>
  <div class="badge" style="left:875px;top:153px;width:108px;height:52px"></div>
  <div class="badge" style="left:992px;top:153px;width:98px;height:52px"></div>
  <div class="badge" style="left:875px;top:213px;width:110px;height:52px"></div>
  <div class="copyright">© 2025 Kelvora Quad. All Rights Reserved.</div>
</footer>

</body>
</html>
```